Web Design Project

We need a website for a new public relations firm offering PR, advertising, media buying, design and social media. Target clients are professional service firms such as lawyers or CPAs. Looks should be clean and look expensive.

Target Market(s)

Professional service firms. Think business to business companies like consultancy firms.

Industry/Entity Type

Professional Service

Colors

Designer to choose colors to be used in the design.

Requirements
Must have
• Site pages for the purpose of design will include Home, Services, Experience, Bios and Contact Us

```html
<!DOCTYPE html>
<html lang="en">
<head>
<meta charset="utf-8">
<title>Halvern Group — Marketing, PR, Advertising</title>
<link href="https://fonts.googleapis.com/css2?family=Quicksand:wght@500;600&family=Nunito+Sans:wght@400;600;700&display=swap" rel="stylesheet">
<style>
:root{
  --teal:#1fa9c1;
  --teal-dark:#178ea3;
  --teal-light:#35c0d6;
  --heading:#1ba6bd;
  --text:#555;
  --white:#fff;
  --line:#dcdcdc;
  --footer:#1c1f24;
  --accent-red:#c0392b;
  --footer-rule:#5b9bd5;
}
*{margin:0;padding:0;box-sizing:border-box}
html,body{width:867px;height:1200px;overflow:hidden;background:var(--white)}
body{position:relative;font-family:"Nunito Sans",Arial,sans-serif;color:var(--text)}
.abs{position:absolute}

.brand{left:72px;top:30px;width:130px}
.brand-name{font-family:"Nunito Sans",sans-serif;font-size:19px;font-weight:400;color:#666;letter-spacing:.5px;line-height:22px}
.brand-tag{font-size:6px;color:#333;margin-top:3px;letter-spacing:.3px}

.main-nav{left:234px;top:24px;width:561px;height:43px;border-radius:5px;
  background:linear-gradient(#3bc3d9,var(--teal-dark));display:flex}
.main-nav a{color:var(--white);text-decoration:none;font-size:10px;font-weight:600;
  display:flex;align-items:center;justify-content:center;border-right:1px solid rgba(0,0,0,.12)}
.main-nav a:last-child{border-right:0}

.hero{left:72px;top:84px;width:723px;height:346px;overflow:hidden;
  background:radial-gradient(ellipse at 55% 40%,#e8f6fb 0%,#9fd3e6 45%,#4d9ec2 100%)}
.hero-caption{position:absolute;left:0;bottom:0;width:100%;height:33px;background:rgba(30,40,50,.55);
  color:var(--white);font-size:16px;padding:6px 15px}
.hero-dots{position:absolute;right:17px;bottom:12px;display:flex;gap:4px}
.hero-dots span{width:8px;height:8px;border-radius:50%;background:var(--white);border:1px solid #333}
.hero-dots span.on{background:#222}
.hero-arrow{position:absolute;top:161px;width:24px;height:24px;border-radius:50%;background:var(--white);
  box-shadow:0 1px 3px rgba(0,0,0,.3)}

.welcome-title{left:0;top:458px;width:867px;text-align:center;font-family:"Quicksand",sans-serif;
  font-weight:600;font-size:22px;color:var(--heading)}
.welcome-text{left:72px;top:497px;width:723px;text-align:center;font-size:9.6px;line-height:18px;color:var(--text)}

.services{left:0;top:593px;width:867px;height:309px;background:var(--teal)}
.services-title{position:absolute;left:70px;top:17px;font-family:"Quicksand",sans-serif;font-weight:600;font-size:18px;color:var(--white)}
.service{position:absolute;top:52px;width:168px;color:var(--white)}
.service-photo{height:122px}
.service h3{font-weight:600;font-size:11.5px;margin:20px 0 8px}
.service p{font-size:8.6px;line-height:14.4px}
.service .more{font-weight:700;color:#111}

.col-title{font-family:"Quicksand",sans-serif;font-weight:600;font-size:14px;color:var(--heading)}
.news-item{position:absolute;left:72px;width:330px}
.date-box{position:absolute;left:2px;top:0;width:26px;height:26px;border:1px solid var(--line);
  font-weight:700;font-size:13px;color:#222;text-align:center;line-height:24px;font-family:Arial,sans-serif}
.date-month{position:absolute;left:2px;top:33px;width:26px;text-align:center;font-size:6px;color:#888}
.news-body{position:absolute;left:39px;top:0;font-family:Arial,sans-serif}
.news-body h4{font-size:8.6px;color:#111;font-weight:700}
.news-body .count{font-size:7px;color:#666;margin-top:3px}
.news-body p{font-size:8.6px;line-height:10.5px;color:#444;margin-top:11px;width:290px}
.news-body a{color:var(--accent-red);text-decoration:none}

.acc{position:absolute;left:440px;width:170px;height:24px;border:1px solid var(--line);
  font-family:Arial,sans-serif;font-size:6.5px;font-weight:700;color:#333;padding:8px 10px;letter-spacing:-.2px}
.acc.open{border-left:3px solid var(--footer-rule)}
.acc i{position:absolute;right:7px;top:6px;width:11px;height:11px;border:1px solid #bbb;border-radius:50%;
  font-style:normal;font-size:9px;color:#999;text-align:center;line-height:9px;font-weight:400}
.acc-panel{left:444px;top:1018px;width:170px;font-family:Arial,sans-serif;font-size:8.4px;line-height:10.5px;color:#555}

.quote{left:623px;top:954px;width:170px;height:66px;border:1px solid var(--line);padding:8px 10px 0 22px;
  font-family:Arial,sans-serif;font-size:8.4px;line-height:10.5px;color:#555}
.quote:before{content:"\201C";position:absolute;left:8px;top:4px;font-size:14px;color:#999}
.avatar{left:643px;top:1028px;width:26px;height:26px;border-radius:50%;background:linear-gradient(#d9dde2,#9aa5b1)}
.person{left:676px;top:1034px;font-family:Arial,sans-serif}
.person b{font-size:8.4px;color:#222}
.person span{display:block;font-size:7px;color:#777;margin-top:3px}

.footer-rule{left:0;top:1112px;width:867px;height:3px;background:var(--footer-rule)}
.footer{left:0;top:1115px;width:867px;height:85px;background:var(--footer)}
.footer-links{left:71px;top:1139px;font-family:Arial,sans-serif;font-size:8.6px;font-weight:700;color:var(--white)}
.copyright{left:71px;top:1158px;font-family:Arial,sans-serif;font-size:8.6px;font-weight:700;color:var(--white)}
.social{left:699px;top:1149px;display:flex;gap:4px}
.social span{width:16px;height:16px}
</style>
</head>
<body>

<div class="abs brand">
  <div class="brand-name">Halvern Group</div>
  <div class="brand-tag">Marketing • PR • Advertising</div>
</div>

<nav class="abs main-nav">
  <a href="#" style="width:103px">Home</a>
  <a href="#" style="width:110px">Services</a>
  <a href="#" style="width:118px">Experience</a>
  <a href="#" style="width:102px">Bios</a>
  <a href="#" style="width:128px">Contact Us</a>
</nav>

<section class="abs hero" role="img" aria-label="Businessman touching floating digital icons for devices, mail, search, shopping and social media">
  <div class="hero-arrow" style="left:27px">
    <svg width="24" height="24"><path d="M14 7l-5 5 5 5" fill="none" stroke="#333" stroke-width="2"/></svg>
  </div>
  <div class="hero-arrow" style="right:27px">
    <svg width="24" height="24"><path d="M10 7l5 5-5 5" fill="none" stroke="#333" stroke-width="2"/></svg>
  </div>
  <div class="hero-caption">Professional service firms such as lawyers or CPAs</div>
  <div class="hero-dots"><span class="on"></span><span></span><span></span></div>
</section>

<h1 class="abs welcome-title">Welcome To Our Comapny</h1>
<p class="abs welcome-text">Lorem ipsum dolor sit amet, consectetuer adipiscing elit, sed diam nonummy nibh euismod tincidunt ut laoreet dolore magna aliquam erat volutpat. Ut wisi enim ad minim veniam, quis nostrud exerci tation ullamcorper suscipit lobortis nisl ut aliquip ex ea commodo consequat. Lorem ipsum dolor sit amet, consectetuer adipiscing elit, sed diam nonummy nibh euismod tincidunt ut laoreet dolore magna aliquam erat volutpat. Ut wisi enim ad minim veniam, quis nostrud exerci tation ullamcorper suscipit lobortis nisl ut aliquip ex ea commodo consequat.</p>

<section class="abs services">
  <h2 class="services-title">Serivces</h2>
  <article class="service" style="left:71px">
    <div class="service-photo" role="img" aria-label="Team of colleagues smiling around a desk" style="background:linear-gradient(135deg,#e9e4df,#b79a85)"></div>
    <h3>PR</h3>
    <p>Lorem ipsum dolor sit amet, consectetuer adipiscing elit, sed diam nonummy nibh euismod tincidunt ut laoreet dolore magna commodo consequat.<br><span class="more">Read More...</span></p>
  </article>
  <article class="service" style="left:254px">
    <div class="service-photo" role="img" aria-label="Planning diagram sketched on paper beside a notebook" style="background:linear-gradient(135deg,#5a4a3a,#e8e4ee)"></div>
    <h3>Advertising</h3>
    <p>Lorem ipsum dolor sit amet, consectetuer adipiscing elit, sed diam nonummy nibh euismod tincidunt ut laoreet dolore magna commodo consequat.<br><span class="more">Read More...</span></p>
  </article>
  <article class="service" style="left:440px">
    <div class="service-photo" role="img" aria-label="Hands typing on a laptop keyboard" style="background:linear-gradient(135deg,#f2f2f2,#c9a99a 55%,#3a3a3a)"></div>
    <h3>Media Buying</h3>
    <p>Lorem ipsum dolor sit amet, consectetuer adipiscing elit, sed diam nonummy nibh euismod tincidunt ut laoreet dolore magna commodo consequat.<br><span class="more">Read More...</span></p>
  </article>
  <article class="service" style="left:623px">
    <div class="service-photo" role="img" aria-label="Hand touching a tablet showing bar charts" style="background:linear-gradient(135deg,#eef3f7,#9ec3e6)"></div>
    <h3>Social Media</h3>
    <p>Lorem ipsum dolor sit amet, consectetuer adipiscing elit, sed diam nonummy nibh euismod tincidunt ut laoreet dolore magna commodo consequat.<br><span class="more">Read More...</span></p>
  </article>
</section>

<h2 class="abs col-title" style="left:72px;top:927px">Latest News</h2>
<div class="news-item" style="top:954px">
  <div class="date-box">21</div><div class="date-month">NOV</div>
  <div class="news-body">
    <h4>This is a Standard Post</h4>
    <div class="count">5 Comments</div>
    <p>Perspiciatis unde omnis iste natus error sit voluptatem accusantium doloremque laudantium, totam rem aperiam. Perspiciatis unde omnis iste natus error sit voluptatem... <a href="#">Read more</a></p>
  </div>
</div>
<div class="news-item" style="top:1036px">
  <div class="date-box">20</div><div class="date-month">OCT</div>
  <div class="news-body">
    <h4>This is a Standard Post</h4>
    <div class="count">5 Comments</div>
    <p>Perspiciatis unde omnis iste natus error sit voluptatem accusantium doloremque laudantium, totam rem aperiam. Perspiciatis unde omnis iste natus error sit voluptatem... <a href="#">Read more</a></p>
  </div>
</div>

<h2 class="abs col-title" style="left:438px;top:927px">More about us</h2>
<div class="acc" style="top:954px">WHO WE ARE?<i>+</i></div>
<div class="acc open" style="top:980px">WHAT WE DO?<i>−</i></div>
<p class="abs acc-panel">Perspiciatis unde omnis iste natus error sit voluptatem accusantium doloremque laudantium, totam rem aperiam. Perspiciatis</p>
<div class="acc" style="top:1072px">WHERE WE DO IT?<i>+</i></div>

<h2 class="abs col-title" style="left:621px;top:927px">Testimonials</h2>
<blockquote class="abs quote">Perspiciatis unde omnis iste natus error sit voluptatem accusantium doloremque laudantium, totam rem aperiam. Perspiciatis</blockquote>
<div class="abs avatar" role="img" aria-label="Portrait of the client"></div>
<div class="abs person"><b>Daniel Hart</b><span>Businessman</span></div>

<div class="abs footer-rule"></div>
<footer class="abs footer"></footer>
<div class="abs footer-links">Home \ Services \ Experience \ Bios \ Contact Us</div>
<div class="abs copyright">Copyright © 2014 Halvern Group. All Rights Reserved</div>
<div class="abs social" aria-label="Social links">
  <span style="background:#3b5a9a"></span>
  <span style="background:#3fa9e0"></span>
  <span style="background:#d34836"></span>
  <span style="background:#c92228"></span>
  <span style="background:#e6e6e6"></span>
</div>

</body>
</html>
```